I have an account on Plumetry through Tanvrik, so the design will need to be built there. I already have a logo, and the design of the website should at least compliment the look of the logo. The placeholder website where the logo can be seen is at www.velmarconsulting.example. The purpose of the website at this point in time is not to drive business, but rather, to have a strong appearance and add some credibility to my already existing business.

The website should have some level of abstraction about it. I prefefer designs and shapes of images of people. The fewer people, the better. No stock photography of people standing around talking to each other.

Number of Pages Required

4 page

Requirements
Must have
• The ability to work on my existing Plume Try Account
Should not have
• Stock photography of people standing around doing "business-y" stuff. That is sooo old and played out, and is the opposite of the type of message I am trying to portray.

```html
<!DOCTYPE html>
<html lang="en">
<head>
<meta charset="utf-8">
<title>Velmar – A Specialized Brand Consultancy</title>
<link href="https://fonts.googleapis.com/css2?family=Montserrat:wght@400;500;600;700&display=swap" rel="stylesheet">
<style>
:root{
  --orange:#f9560f;
  --orange-dark:#d9420a;
  --charcoal:#4a4a4a;
  --charcoal-deep:#3d3d3d;
  --panel:rgba(88,88,88,.88);
  --white:#ffffff;
  --muted:#e4e4e4;
}
*{margin:0;padding:0;box-sizing:border-box}
html,body{width:1200px;height:4675px;overflow:hidden}
body{font-family:'Montserrat',sans-serif;background:var(--charcoal);color:var(--white);position:relative}
.abs{position:absolute}
.photo{position:absolute;left:0;width:1200px}
.shade{position:absolute;inset:0;background:rgba(40,40,40,.55)}
.btn{display:inline-flex;align-items:center;gap:8px;background:var(--orange);color:var(--white);font-weight:600;text-transform:uppercase;border-radius:24px;font-size:15px;padding:0 22px;height:48px}
.section-title{position:absolute;left:0;width:1200px;text-align:center;font-size:35px;font-weight:500;letter-spacing:1px;text-transform:uppercase}
.lead{position:absolute;left:180px;width:840px;text-align:center;font-size:16px;line-height:30px;color:var(--muted)}
.brand-mark{display:flex;align-items:center;gap:14px}
.brand-square{width:78px;height:78px;background:var(--white)}
.brand-name{font-weight:500;color:var(--orange);text-transform:uppercase;letter-spacing:1px}

/* header */
.topbar{top:0;left:0;width:1200px;height:118px;background:var(--charcoal)}
.support{left:92px;top:32px;display:flex;gap:12px;align-items:center}
.support small{display:block;color:var(--orange);font-size:14px;font-weight:500}
.support strong{font-size:22px;font-weight:700}
.nav{top:118px;left:0;width:1200px;height:62px;background:var(--orange);display:flex;justify-content:center;gap:50px;align-items:center;font-size:16px;text-transform:uppercase}
/* hero */
.hero-text{right:50px;top:310px;text-align:right;width:600px}
.hero-text h1{font-size:54px;font-weight:400;letter-spacing:1px}
.hero-text h2{font-size:29px;font-weight:700;margin-top:4px}
.hero-text p{font-size:17px;line-height:34px;margin-top:16px;margin-left:auto;width:560px}
/* about */
.about-circle{left:104px;top:875px;width:445px;height:445px;border-radius:50%;border:10px solid var(--orange);background:radial-gradient(circle at 50% 45%,#2f6fb8,#10234a 70%)}
.about-text{left:583px;top:948px;width:527px}
.about-text h2{font-size:37px;font-weight:500;text-transform:uppercase}
.about-text p{font-size:15.5px;line-height:30px;color:var(--muted);text-align:justify;margin:16px 0 22px}
.about-text .btn{border-radius:0;height:40px;font-size:15px}
/* cards */
.card{position:absolute;width:322px;background:var(--panel);text-align:center;padding:18px 20px}
.card h3{color:var(--orange);font-weight:500;text-transform:uppercase;font-size:19px;margin-top:8px}
.card p{font-size:13px;line-height:22px;margin-top:6px}
.card .more{color:var(--orange);font-size:13px;font-weight:600;text-transform:uppercase;margin-top:8px}
.arrow-nav{position:absolute}
/* approach */
.step{position:absolute;width:240px;text-align:center}
.step span{display:block;margin-top:14px;font-size:22px;text-transform:uppercase}
/* testimonials */
.quote{left:180px;top:3140px;width:840px;text-align:center}
.quote p{font-size:20px;line-height:38px;margin-top:20px}
.quote strong{display:block;margin-top:22px;font-size:17px}
/* blog */
.post{position:absolute;width:328px}
.post .img{height:197px;position:relative}
.post .date{position:absolute;left:10px;bottom:-10px;background:var(--orange);font-size:12px;padding:5px 10px}
.post h3{font-size:19px;font-weight:500;text-transform:uppercase;margin-top:32px}
.post p{font-size:13px;line-height:22px;color:var(--muted);margin-top:8px}
.post .read{font-size:13px;font-weight:700;text-transform:uppercase;margin-top:12px}
/* footer */
.contact{position:absolute;width:300px;text-align:center;font-size:18px;line-height:28px}
.contact .icon{width:88px;height:88px;border-radius:50%;background:var(--orange);margin:0 auto 14px;display:flex;align-items:center;justify-content:center}
.foot-links{top:4535px;left:0;width:1200px;text-align:center;font-size:17px}
.copyright{top:4578px;left:0;width:1200px;text-align:center;font-size:14px;color:var(--muted)}
.socials{top:4618px;left:0;width:1200px;display:flex;justify-content:center;gap:10px}
.socials i{width:34px;height:34px;border:2px solid var(--white);border-radius:50%}
</style>
</head>
<body>

<!-- header -->
<header class="abs topbar">
  <div class="abs support">
    <svg width="44" height="44" viewBox="0 0 44 44"><circle cx="22" cy="22" r="19" fill="none" stroke="var(--orange)" stroke-width="3"/><path d="M15 13l5 0 2 6-3 2c1 3 4 6 7 7l2-3 6 2 0 5c-11 1-20-8-19-19z" fill="var(--orange)"/></svg>
    <div><small>Support Call us</small><strong>1-800-555-0142</strong></div>
  </div>
  <div class="abs brand-mark" style="left:445px;top:14px"><div class="brand-square" style="width:88px;height:88px"></div><span class="brand-name" style="font-size:44px">Velmar</span></div>
  <div class="abs btn" style="left:850px;top:34px;height:52px;padding:0 26px">
    <svg width="16" height="16" viewBox="0 0 16 16"><rect x="1" y="3" width="14" height="12" fill="none" stroke="#fff" stroke-width="2"/><path d="M1 7h14M5 1v4M11 1v4" stroke="#fff" stroke-width="2"/></svg>Book an appointment</div>
</header>
<nav class="abs nav"><span>Home</span><span>About Us</span><span>Our Services</span><span>Our Approach</span><span>Testimonials</span><span>Contact Us</span></nav>

<!-- hero -->
<div class="photo" style="top:180px;height:590px;background:linear-gradient(100deg,#2c3440 0%,#8e98a3 45%,#d8dde2 70%,#6a7480 100%)" role="img" aria-label="Two consultants in dark suits meeting across a desk in a bright office"></div>
<div class="abs hero-text">
  <h1>VELMAR</h1>
  <h2>A Specialized Brand Consultancy.</h2>
  <p>We help our clients identify and develop protectable source identifiers through asset creation-oriented strategies.</p>
  <div class="btn" style="margin-top:20px"><svg width="16" height="16" viewBox="0 0 16 16"><rect x="1" y="3" width="14" height="12" fill="none" stroke="#fff" stroke-width="2"/><path d="M1 7h14M5 1v4M11 1v4" stroke="#fff" stroke-width="2"/></svg>Book an appointment</div>
</div>
<svg class="abs" style="left:0;top:690px" width="1200" height="90" viewBox="0 0 1200 90"><path d="M0 60 Q300 10 600 45 T1200 20 V90 H0Z" fill="var(--charcoal)"/><path d="M0 60 Q300 10 600 45 T1200 20 L1200 30 Q900 60 600 58 T0 80Z" fill="var(--orange)"/></svg>

<!-- about -->
<div class="abs about-circle" role="img" aria-label="Hand touching a glowing blue digital chart and network diagram"></div>
<div class="abs about-text">
  <h2>About Us</h2>
  <p>Sed ut perspiciatis unde omnis iste natus error sit voluptatem accusantium doloremque laudantium, totam rem aperiam, eaque ipsa quae ab illo inventore veritatis et quasi architecto beatae vitae dicta sunt explicabo. Nemo enim ipsam voluptatem quia voluptas sit aspernatur aut odit aut fugit, sed quia consequuntur magni dolores eos qui ratione voluptatem sequi nesciunt.</p>
  <span class="btn">Read More</span>
</div>

<!-- services -->
<div class="photo" style="top:1440px;height:650px;background:linear-gradient(120deg,#3a3530,#6b6258 50%,#2f2c2a)" role="img" aria-label="Blurred office interior behind the services section"><div class="shade"></div></div>
<svg class="abs" style="left:0;top:1410px" width="1200" height="70" viewBox="0 0 1200 70"><path d="M0 0 H1200 V20 Q900 50 600 40 T0 60Z" fill="var(--charcoal)"/><path d="M600 40 Q900 50 1200 20 V32 Q900 60 600 50Z" fill="var(--orange)"/></svg>
<h2 class="section-title" style="top:1562px">Our Services</h2>
<p class="lead" style="top:1618px">At vero eos et accusamus et iusto odio dignissimos ducimus qui blanditiis praesentium voluptatum deleniti atque corrupti quos dolores et quas molestias excepturi sint</p>
<svg class="arrow-nav" style="left:36px;top:1822px" width="40" height="24" viewBox="0 0 40 24"><path d="M38 12H4M14 2L4 12l10 10" fill="none" stroke="#fff" stroke-width="3"/></svg>
<svg class="arrow-nav" style="left:1124px;top:1822px" width="40" height="24" viewBox="0 0 40 24"><path d="M2 12h34M26 2l10 10-10 10" fill="none" stroke="#fff" stroke-width="3"/></svg>
<div class="card" style="left:90px;top:1708px">
  <svg width="74" height="74" viewBox="0 0 74 74" fill="none" stroke="var(--orange)" stroke-width="3"><circle cx="30" cy="30" r="20"/><path d="M44 44l22 22M20 36l7-8 6 5 8-10"/></svg>
  <h3>Brand Research</h3><p>Sed ut perspiciatis unde omnis iste natus error sit voluptatem accusantium doloremque laudantium</p><div class="more">Read more →</div>
</div>
<div class="card" style="left:437px;top:1708px">
  <svg width="74" height="74" viewBox="0 0 74 74" fill="none" stroke="var(--orange)" stroke-width="3"><circle cx="37" cy="37" r="28"/><circle cx="22" cy="24" r="5"/><circle cx="52" cy="50" r="5"/><path d="M26 28l22 18M48 20l8 8M56 20l-8 8M18 46l8 8M26 46l-8 8"/></svg>
  <h3>Brand Strategy</h3><p>Sed ut perspiciatis unde omnis iste natus error sit voluptatem accusantium doloremque laudantium</p><div class="more">Read more →</div>
</div>
<div class="card" style="left:786px;top:1708px">
  <svg width="74" height="74" viewBox="0 0 74 74" fill="none" stroke="var(--orange)" stroke-width="3"><circle cx="37" cy="37" r="12"/><circle cx="37" cy="37" r="4"/><path d="M37 19v-8M37 55v8M19 37h-8M55 37h8M24 24l-6-6M50 50l6 6M50 24l6-6M24 50l-6 6"/></svg>
  <h3>Brand Management</h3><p>Sed ut perspiciatis unde omnis iste natus error sit voluptatem accusantium doloremque laudantium</p><div class="more">Read more →</div>
</div>
<svg class="abs" style="left:0;top:2050px" width="1200" height="60" viewBox="0 0 1200 60"><path d="M0 20 Q400 60 800 30 T1200 30 V60 H0Z" fill="var(--charcoal)"/></svg>

<!-- approach -->
<h2 class="section-title" style="top:2206px">Our Approach</h2>
<p class="lead" style="top:2262px;left:140px;width:920px">Sed ut perspiciatis unde omnis iste natus error sit voluptatem accusantium doloremque laudantium, totam rem aperiam, eaque ipsa quae ab illo inventore veritatis et quasi architecto beatae vitae dicta sunt explicabo. Nemo enim ipsam voluptatem quia voluptas sit aspernatur aut odit aut fugit, sed quia consequuntur magni dolores eos qui ratione voluptatem sequi nesciunt.</p>
<div class="step" style="left:89px;top:2420px">
  <svg width="240" height="240" viewBox="0 0 240 240"><circle cx="120" cy="120" r="114" fill="none" stroke="var(--orange)" stroke-width="4"/><circle cx="120" cy="120" r="96" fill="none" stroke="var(--orange)" stroke-width="14"/><g fill="none" stroke="#fff" stroke-width="4"><path d="M70 120q50-50 100 0q-50 50-100 0z"/><circle cx="120" cy="120" r="16"/><path d="M80 88h-10v-10M160 88h10v-10M80 152h-10v10M160 152h10v10"/></g></svg>
  <span>Envision</span></div>
<div class="step" style="left:348px;top:2420px">
  <svg width="240" height="240" viewBox="0 0 240 240"><circle cx="120" cy="120" r="114" fill="none" stroke="var(--orange)" stroke-width="4"/><circle cx="120" cy="120" r="96" fill="none" stroke="var(--orange)" stroke-width="14"/><g fill="none" stroke="#fff" stroke-width="4"><path d="M82 160l30-30 14 14-30 30z"/><path d="M112 130l24-24 14 14-24 24z"/><path d="M146 92l4-14M158 104l14-4M156 86l10-10"/></g></svg>
  <span>Explore</span></div>
<div class="step" style="left:609px;top:2420px">
  <svg width="240" height="240" viewBox="0 0 240 240"><circle cx="120" cy="120" r="114" fill="none" stroke="var(--orange)" stroke-width="4"/><circle cx="120" cy="120" r="96" fill="none" stroke="var(--orange)" stroke-width="14"/><g fill="none" stroke="#fff" stroke-width="4"><rect x="80" y="76" width="62" height="82"/><path d="M92 140v-16M106 140v-26M120 140v-20M92 94h38"/><rect x="130" y="108" width="36" height="50"/><path d="M138 122h20M138 134h20M138 146h20"/></g></svg>
  <span>Evaluate</span></div>
<div class="step" style="left:869px;top:2420px">
  <svg width="240" height="240" viewBox="0 0 240 240"><circle cx="120" cy="120" r="114" fill="none" stroke="var(--orange)" stroke-width="4"/><circle cx="120" cy="120" r="96" fill="none" stroke="var(--orange)" stroke-width="14"/><g fill="none" stroke="#fff" stroke-width="4"><rect x="78" y="80" width="84" height="66"/><path d="M104 160h32M120 146v14"/><circle cx="120" cy="112" r="14"/><path d="M120 92v6M120 126v6M100 112h6M134 112h6"/></g></svg>
  <span>Execute</span></div>

<!-- testimonials -->
<svg class="abs" style="left:0;top:2780px" width="1200" height="60" viewBox="0 0 1200 60"><path d="M0 40 Q600 0 1200 20 V30 Q600 10 0 50Z" fill="var(--orange)"/></svg>
<div class="photo" style="top:2820px;height:660px;background:linear-gradient(90deg,#3c3a38,#7a706a 45%,#4a4644)" role="img" aria-label="Softly blurred business meeting room behind the testimonials"><div class="shade"></div></div>
<h2 class="section-title" style="top:3008px">Testimonials</h2>
<svg class="arrow-nav" style="left:70px;top:3130px" width="66" height="34" viewBox="0 0 66 34"><path d="M64 17H4M18 3L4 17l14 14" fill="none" stroke="#fff" stroke-width="4"/></svg>
<svg class="arrow-nav" style="left:1064px;top:3130px" width="66" height="34" viewBox="0 0 66 34"><path d="M2 17h60M48 3l14 14-14 14" fill="none" stroke="#fff" stroke-width="4"/></svg>
<div class="abs quote">
  <svg width="50" height="40" viewBox="0 0 50 40"><path d="M4 38V22Q4 6 20 2v8Q12 14 12 20h10v18zM28 38V22Q28 6 44 2v8Q36 14 36 20h10v18z" fill="#fff"/></svg>
  <p>Sed ut perspiciatis unde omnis iste natus error sit voluptatem accusantium doloremque laudantium, totam rem aperiam, eaque ipsa quae ab illo inventore veritatis et quasi architecto beatae vitae dicta sunt explicabo.</p>
  <strong>Dana Whitfield</strong>
</div>
<svg class="abs" style="left:0;top:3420px" width="1200" height="90" viewBox="0 0 1200 90"><path d="M0 40 Q300 80 600 50 T1200 40 V90 H0Z" fill="var(--charcoal)"/><path d="M0 30 Q300 70 600 45 L600 55 Q300 85 0 50Z" fill="var(--orange)"/></svg>

<!-- blog -->
<h2 class="section-title" style="top:3580px">Our Blog</h2>
<div class="post" style="left:90px;top:3653px">
  <div class="img" style="background:linear-gradient(135deg,#c9cdd3,#6f7884)" role="img" aria-label="Hands reviewing charts on a desk"><span class="date">Oct 27 2018</span></div>
  <h3>Sed ut perspiciatis und</h3><p>Sed ut perspiciatis unde omnis iste natus error sit voluptatem accusantium doloremque laudantium, totam rem aperiam, eaque ipsa quae ab illo</p><div class="read">Read more</div></div>
<div class="post" style="left:436px;top:3653px">
  <div class="img" style="background:linear-gradient(135deg,#e6e3de,#8c857b)" role="img" aria-label="Speaker presenting to a seated audience"><span class="date">Oct 27 2018</span></div>
  <h3>Sed ut perspiciatis und</h3><p>Sed ut perspiciatis unde omnis iste natus error sit voluptatem accusantium doloremque laudantium, totam rem aperiam, eaque ipsa quae ab illo</p><div class="read">Read more</div></div>
<div class="post" style="left:782px;top:3653px">
  <div class="img" style="background:linear-gradient(135deg,#7c8896,#2c333d)" role="img" aria-label="Audience watching a presentation screen"><span class="date">Oct 27 2018</span></div>
  <h3>Sed ut perspiciatis und</h3><p>Sed ut perspiciatis unde omnis iste natus error sit voluptatem accusantium doloremque laudantium, totam rem aperiam, eaque ipsa quae ab illo</p><div class="read">Read more</div></div>

<!-- footer -->
<div class="photo" style="top:4115px;height:560px;background:linear-gradient(110deg,#2e2b29,#5a5450 50%,#2b2927)" role="img" aria-label="Dim blurred conference room behind the footer"><div class="shade" style="background:rgba(30,30,30,.6)"></div></div>
<svg class="abs" style="left:0;top:4085px" width="1200" height="70" viewBox="0 0 1200 70"><path d="M0 0 H1200 V20 Q700 60 0 40Z" fill="var(--charcoal)"/><path d="M0 40 Q700 60 1200 20 V30 Q700 72 0 50Z" fill="var(--orange)"/></svg>
<div class="abs brand-mark" style="left:522px;top:4192px;flex-direction:column;gap:16px;width:156px">
  <div class="brand-square" style="width:84px;height:84px"></div><span class="brand-name" style="font-size:34px">Velmar</span></div>
<div class="contact" style="left:150px;top:4362px"><div class="icon"><svg width="40" height="40" viewBox="0 0 40 40" fill="none" stroke="#fff" stroke-width="3"><path d="M20 36S8 22 8 15a12 12 0 0124 0c0 7-12 21-12 21z"/><circle cx="20" cy="15" r="4"/></svg></div>48 Larkfield Ave.<br>Maple Hollow, VA 20190</div>
<div class="contact" style="left:450px;top:4362px"><div class="icon"><svg width="40" height="40" viewBox="0 0 40 40"><path d="M10 6h8l3 8-4 3c2 4 5 7 9 9l3-4 8 3v8C21 34 6 19 10 6z" fill="#fff"/></svg></div>Phone:<br>800 555 0142</div>
<div class="contact" style="left:750px;top:4362px"><div class="icon"><svg width="42" height="32" viewBox="0 0 42 32" fill="none" stroke="#fff" stroke-width="3"><rect x="2" y="2" width="38" height="28"/><path d="M2 2l19 16L40 2"/></svg></div>Email:<br>info@velmar.example</div>
<div class="abs foot-links">Home &nbsp;|&nbsp; About Us &nbsp;|&nbsp; Our Services &nbsp;|&nbsp; Our Approach &nbsp;|&nbsp; Blog &nbsp;|&nbsp; Testimonials &nbsp;|&nbsp; Contact Us</div>
<div class="abs copyright">© 2019 Company Name · All right reserved</div>
<div class="abs socials"><i></i><i></i><i></i><i></i></div>

</body>
</html>
```